Oil Field Service company needs professional business cards

Looking to clean up our current company business cards and look a little more professional. Harlow Tubular Services is a US based company that services the oil field. We deal with engineers, managers and oil rigs....................................................................................................................................................................................................................................................................................................................................................................................................

Target Market(s)

Oil and Gas professionals

Industry/Entity Type

Oil And Gas

Contact Information for Business Card

See attached photo as example

Font styles to use
Sans Serif

Colors
ec1f27

Requirements
Must have
• Company Logo, Name, Title, Cell, Office, Fax, Email.
• See attached photo
Nice to have
• External CRT, Internal CRT, Casing Crews, Torque Turn, Laydown Machine
Should not have
• Do not introduce any new pictures and keep it professional looking

```html
<!DOCTYPE html>
<html lang="en">
<head>
<meta charset="utf-8">
<title>Harlow Tubular Services – Business Card</title>
<link rel="stylesheet" href="https://fonts.googleapis.com/css2?family=Roboto:wght@400;500;700;900&family=Roboto+Condensed:wght@400&display=swap">
<style>
  :root {
    --navy: #2b3640;
    --red: #ec1f27;
    --paper: #ffffff;
    --ink: #3a4148;
    --backdrop: #e6e7e8;
  }
  * { box-sizing: border-box; margin: 0; padding: 0; }
  html, body { width: 1200px; height: 873px; overflow: hidden; }
  body {
    background: var(--backdrop);
    font-family: "Roboto", Arial, sans-serif;
    position: relative;
  }
  .card {
    position: absolute;
    top: 296px;
    width: 500px;
    height: 281px;
    box-shadow: 0 6px 18px rgba(0,0,0,0.18);
    overflow: hidden;
  }
  .card-front { left: 80px; background: var(--navy); }
  .card-back { left: 620px; background: var(--paper); }

  .wordmark {
    position: absolute;
    font-weight: 900;
    text-transform: uppercase;
    white-space: nowrap;
    display: flex;
    align-items: center;
    gap: 10px;
  }
  .wordmark .dot {
    width: 14px; height: 14px; border-radius: 50%;
    background: var(--red);
    flex: none;
  }
  .card-front .wordmark {
    top: 112px;
    left: 0; right: 0;
    justify-content: center;
    color: var(--paper);
    font-size: 27px;
    letter-spacing: 1px;
  }
  .card-back .wordmark {
    top: 54px;
    left: 27px;
    color: var(--navy);
    font-size: 18px;
    line-height: 24px;
    letter-spacing: 0.5px;
    gap: 8px;
  }
  .card-back .wordmark .dot { width: 11px; height: 11px; }

  .services-band {
    position: absolute;
    left: 0; right: 0;
    top: 239px;
    height: 17px;
    background: var(--red);
    color: var(--paper);
    font-family: "Roboto Condensed", Arial, sans-serif;
    font-size: 11.5px;
    line-height: 17px;
    text-align: center;
    white-space: nowrap;
  }
  .services-band .sep { margin: 0 6px; }

  .name-band {
    position: absolute;
    left: 0; right: 0;
    top: 150px;
    height: 26px;
    background: var(--navy);
    padding-left: 27px;
    line-height: 26px;
    white-space: nowrap;
  }
  .name-band .person { color: var(--paper); font-weight: 700; font-size: 15px; }
  .name-band .role { color: var(--red); font-size: 12px; }

  .contact {
    position: absolute;
    list-style: none;
    font-size: 12.5px;
    color: var(--ink);
    line-height: 16px;
    white-space: nowrap;
  }
  .contact li { display: flex; align-items: center; gap: 6px; }
  .contact svg { width: 10px; height: 10px; flex: none; fill: var(--red); }
  .contact-personal { left: 27px; top: 226px; }
  .contact-office { left: 322px; top: 196px; }
</style>
</head>
<body>

<section class="card card-front" aria-label="Card front">
  <div class="wordmark"><span class="dot"></span>Harlow Tubular Services</div>
  <div class="services-band">
    External CRT<span class="sep">|</span>Internal CRT<span class="sep">|</span>Casing Crews<span class="sep">|</span>Torque Turn<span class="sep">|</span>Laydown Machine
  </div>
</section>

<section class="card card-back" aria-label="Card back">
  <div class="wordmark"><span class="dot"></span>Harlow Tubular Services</div>

  <div class="name-band">
    <span class="person">Wade Pemberton</span> <span class="role">| Area Manager</span>
  </div>

  <ul class="contact contact-personal">
    <li>
      <svg viewBox="0 0 10 10"><path d="M3 0h4a1 1 0 0 1 1 1v8a1 1 0 0 1-1 1H3a1 1 0 0 1-1-1V1a1 1 0 0 1 1-1zm0 1.5v6h4v-6z"/></svg>
      (555) 218-4476
    </li>
    <li>
      <svg viewBox="0 0 10 10"><path d="M0 2h10v6H0zm1 1v.4l4 2.4 4-2.4V3z"/></svg>
      wpemberton@harlowtubular.com
    </li>
  </ul>

  <ul class="contact contact-office">
    <li>
      <svg viewBox="0 0 10 10"><path d="M5 0a3.4 3.4 0 0 1 3.4 3.4C8.4 6 5 10 5 10S1.6 6 1.6 3.4A3.4 3.4 0 0 1 5 0zm0 2a1.4 1.4 0 1 0 0 2.8A1.4 1.4 0 0 0 5 2z"/></svg>
      Ridgeton, OK 73990
    </li>
    <li>
      <svg viewBox="0 0 10 10"><path d="M2.2 0.5l1.6 2.2-1 1.1c.7 1.5 1.9 2.7 3.4 3.4l1.1-1 2.2 1.6-1 1.9C4.8 9.4.6 5.2.3 1.5z"/></svg>
      (555) 310-5700
    </li>
    <li>
      <svg viewBox="0 0 10 10"><path d="M2.5 0h5v3h-5zM0 3.5h10v4.5H8V6H2v2H0zM2.5 6.8h5V10h-5z"/></svg>
      (555) 310-3230
    </li>
    <li>
      <svg viewBox="0 0 10 10"><path d="M5 0a5 5 0 1 1 0 10A5 5 0 0 1 5 0zm0 1.2C4.2 2.2 3.8 3.5 3.8 5s.4 2.8 1.2 3.8C5.8 7.8 6.2 6.5 6.2 5S5.8 2.2 5 1.2zM1.3 4.5h7.4v1H1.3z"/></svg>
      www.harlowtubular.com
    </li>
  </ul>
</section>

</body>
</html>
```